Letterhead and Business card for Construction company

We need a letterhead and business card with our new company logo. We are based in NY. We develop and build properties.

The design should incorporate some unique feature from the logo (shape, font...). it should look like an extension from it.

Design should be clean and elegant, professional, not too busy.

The letterhead should include:
Logo (attached)
Address
Phone
Email

Please find the attached logo images and AI file.

Target Market(s)

Construction industry professionals

Industry/Entity Type

Construction, Development

Font styles to use
Sans Serif

Colors

Designer to choose colors to be used in the design.

Requirements
Must have
• Design should incorporate logo elements, additional assets are welcome. I'd like to see some other shapes / images invorporated too.

```html
<!DOCTYPE html>
<html lang="en">
<head>
<meta charset="utf-8">
<title>Halden Contracting — Business Card</title>
<link rel="stylesheet" href="https://fonts.googleapis.com/css2?family=Arimo:wght@400;700&display=swap">
<style>
  :root {
    --backdrop: #2b2b2b;
    --card: #0d0d0d;
    --ink: #f2f2f2;
    --mark: #e4e6e5;
    --accent: #f07d1a;
    --rule: #555555;
    --silver: #cfd1d1;
  }
  * { margin: 0; padding: 0; box-sizing: border-box; }
  html, body {
    width: 1200px;
    height: 900px;
    overflow: hidden;
    background: var(--backdrop);
    font-family: "Arimo", Arial, sans-serif;
  }
  .stage {
    position: relative;
    width: 1200px;
    height: 900px;
  }
  .card {
    position: absolute;
    top: 302px;
    width: 520px;
    height: 296px;
    background: var(--card);
    border-radius: 22px;
    box-shadow: 0 18px 40px rgba(0,0,0,0.45);
    overflow: hidden;
  }
  .card--front { left: 50px; }
  .card--back { left: 630px; }

  /* Front */
  .brand {
    position: absolute;
    left: 44px;
    top: 104px;
    width: 200px;
    display: flex;
    align-items: center;
    gap: 12px;
  }
  .brand__square {
    width: 26px;
    height: 26px;
    background: var(--mark);
    flex: none;
  }
  .brand__name {
    color: var(--mark);
    font-weight: 700;
    font-size: 22px;
    line-height: 1.05;
    letter-spacing: 1px;
    text-transform: uppercase;
  }
  .divider {
    position: absolute;
    left: 262px;
    top: 58px;
    width: 1px;
    height: 180px;
    background: var(--rule);
  }
  .details {
    position: absolute;
    left: 286px;
    top: 62px;
    color: var(--ink);
  }
  .person__name {
    color: var(--accent);
    font-weight: 700;
    font-size: 17px;
    letter-spacing: 0.3px;
    text-transform: uppercase;
    line-height: 1.1;
  }
  .person__role {
    font-size: 13px;
    margin-top: 2px;
  }
  .contact {
    list-style: none;
    margin-top: 14px;
  }
  .contact__item {
    display: flex;
    align-items: center;
    gap: 8px;
    font-size: 13px;
    line-height: 19px;
  }
  .contact__icon {
    width: 12px;
    height: 12px;
    flex: none;
  }
  .contact__highlight { color: var(--accent); }
  .address {
    margin-top: 14px;
    padding-left: 20px;
    font-size: 13px;
    line-height: 17px;
    font-style: normal;
  }

  /* Back */
  .brand--back {
    position: absolute;
    inset: 0;
    display: flex;
    align-items: center;
    justify-content: center;
    gap: 14px;
  }
  .brand--back .brand__square {
    width: 32px;
    height: 32px;
    background: var(--silver);
  }
  .brand--back .brand__name {
    color: var(--silver);
    font-size: 28px;
  }
</style>
</head>
<body>
<main class="stage">

  <section class="card card--front" aria-label="Business card front">
    <div class="brand">
      <span class="brand__square"></span>
      <span class="brand__name">Halden<br>Contracting</span>
    </div>

    <div class="divider"></div>

    <div class="details">
      <p class="person__name">Marcus Ellery</p>
      <p class="person__role">Managing Director</p>

      <ul class="contact">
        <li class="contact__item">
          <svg class="contact__icon" viewBox="0 0 24 24" aria-hidden="true">
            <path fill="#f07d1a" d="M6.6 10.8a15.1 15.1 0 0 0 6.6 6.6l2.2-2.2c.3-.3.7-.4 1-.2 1.1.4 2.3.6 3.6.6.6 0 1 .4 1 1V20c0 .6-.4 1-1 1A17 17 0 0 1 3 4c0-.6.4-1 1-1h3.5c.6 0 1 .4 1 1 0 1.3.2 2.5.6 3.6.1.3 0 .7-.2 1z"/>
          </svg>
          <span>044-555 201 347</span>
        </li>
        <li class="contact__item">
          <svg class="contact__icon" viewBox="0 0 24 24" aria-hidden="true">
            <rect x="2" y="5" width="20" height="14" fill="#f07d1a"/>
            <path d="M2 5l10 8 10-8" fill="none" stroke="#0d0d0d" stroke-width="2"/>
          </svg>
          <span>info@haldenbuild.com</span>
        </li>
        <li class="contact__item">
          <svg class="contact__icon" viewBox="0 0 24 24" aria-hidden="true">
            <g fill="none" stroke="#f07d1a" stroke-width="2">
              <circle cx="12" cy="12" r="9"/>
              <ellipse cx="12" cy="12" rx="4" ry="9"/>
              <path d="M3 12h18M5 7h14M5 17h14"/>
            </g>
          </svg>
          <span>www.<span class="contact__highlight">haldenbuild</span>.com</span>
        </li>
      </ul>

      <address class="address">
        118, Mercer Street New York<br>
        10012,United States
      </address>
    </div>
  </section>

  <section class="card card--back" aria-label="Business card back">
    <div class="brand brand--back">
      <span class="brand__square"></span>
      <span class="brand__name">Halden<br>Contracting</span>
    </div>
  </section>

</main>
</body>
</html>
```